Property Management company

We need a design for our company Maplecrest Elder Residences. We are complex of apartments that we manage and operate. We do like the colors green or blue

Industry/Entity Type

Property Management,

Requirements
Must have
• color
Nice to have
• maybe be able to use as a watermark

```html
<!DOCTYPE html>
<html lang="en">
<head>
<meta charset="utf-8">
<title>Maplecrest Elder Residences – Letterhead</title>
<link rel="stylesheet" href="https://fonts.googleapis.com/css2?family=Marcellus&family=Montserrat:wght@400;500&display=swap">
<style>
  :root {
    --backdrop: #cfe5d2;
    --paper: #ffffff;
    --brand-green: #0f6b35;
    --watermark-green: #aecdb2;
    --accent-blue: #1a86cc;
    --ink: #1d2a33;
  }
  * { margin: 0; padding: 0; box-sizing: border-box; }
  html, body {
    width: 1200px; height: 1200px; overflow: hidden;
    background: var(--backdrop);
  }
  .letterhead {
    position: absolute; left: 230px; top: 125px;
    width: 740px; height: 950px;
    background: var(--paper);
    box-shadow: 0 2px 8px rgba(0,0,0,0.18);
  }
  .masthead {
    position: absolute; top: 40px; left: 0; right: 0;
    display: flex; flex-direction: column; align-items: center;
  }
  .masthead__dot {
    width: 14px; height: 14px; border-radius: 50%;
    background: var(--brand-green); margin-bottom: 14px;
  }
  .brand-name {
    font-family: "Marcellus", serif; font-weight: 400;
    color: var(--brand-green); text-align: center; line-height: 1.05;
  }
  .masthead .brand-name__main { font-size: 40px; display: block; }
  .masthead .brand-name__sub { font-size: 17px; letter-spacing: 5px; display: block; margin-top: 8px; }
  .watermark {
    position: absolute; top: 390px; left: 0; right: 0;
    text-align: center;
  }
  .watermark .brand-name { color: var(--watermark-green); }
  .watermark .brand-name__main { font-size: 74px; display: block; }
  .watermark .brand-name__sub { font-size: 28px; letter-spacing: 9px; display: block; margin-top: 18px; }
  .footer-rule {
    position: absolute; top: 827px; left: 0; width: 740px; height: 24px;
  }
  .contact-line {
    position: absolute; top: 858px; left: 0; right: 0;
    text-align: center;
    font-family: "Montserrat", sans-serif; font-size: 11.5px; color: var(--ink);
  }
  .contact-line .sep { margin: 0 10px; }
  .address-line {
    position: absolute; top: 882px; left: 0; right: 0;
    text-align: center;
    font-family: "Montserrat", sans-serif; font-weight: 500;
    font-size: 11.5px; letter-spacing: 1.3px; color: var(--ink);
  }
</style>
</head>
<body>
  <main class="letterhead">
    <header class="masthead">
      <span class="masthead__dot"></span>
      <p class="brand-name">
        <span class="brand-name__main">MAPLECREST</span>
        <span class="brand-name__sub">ELDER RESIDENCES</span>
      </p>
    </header>

    <div class="watermark" aria-hidden="true">
      <p class="brand-name">
        <span class="brand-name__main">MAPLECREST</span>
        <span class="brand-name__sub">ELDER RESIDENCES</span>
      </p>
    </div>

    <svg class="footer-rule" viewBox="0 0 740 24" aria-hidden="true">
      <g stroke="#1a86cc" stroke-width="1.2" fill="#1a86cc">
        <line x1="0" y1="12" x2="296" y2="12"/>
        <circle cx="296" cy="12" r="2" stroke="none"/>
        <line x1="441" y1="12" x2="740" y2="12"/>
        <circle cx="441" cy="12" r="2" stroke="none"/>
      </g>
      <g fill="#1a86cc">
        <circle cx="322" cy="9" r="10"/>
        <circle cx="353" cy="9" r="10"/>
        <circle cx="385" cy="9" r="10"/>
        <circle cx="416" cy="9" r="10"/>
      </g>
      <!-- phone -->
      <path d="M318.5 4.5c.6-.6 1.3-.5 1.6 0l1 1.6c.3.5.2 1-.2 1.3l-.6.5c.4 1 1.4 2 2.4 2.4l.5-.6c.3-.4.8-.5 1.3-.2l1.6 1c.5.3.6 1 0 1.6-1 1-2.2 1.2-3.6.4-1.7-1-3-2.3-4-4-.8-1.4-.6-2.6.4-3.6z" fill="#fff"/>
      <!-- fax -->
      <g fill="#fff">
        <rect x="348" y="6" width="2.4" height="8" rx="0.6"/>
        <rect x="351.5" y="7" width="6.5" height="7" rx="0.8"/>
        <rect x="352.5" y="4" width="4.5" height="3" fill="none" stroke="#fff" stroke-width="0.9"/>
      </g>
      <g fill="#1a86cc">
        <rect x="352.8" y="9" width="1.2" height="1.1"/><rect x="355" y="9" width="1.2" height="1.1"/>
        <rect x="352.8" y="11.2" width="1.2" height="1.1"/><rect x="355" y="11.2" width="1.2" height="1.1"/>
      </g>
      <!-- envelope -->
      <rect x="380" y="5.5" width="10" height="7" rx="1" fill="#fff"/>
      <path d="M380.5 6.2l4.5 3.4 4.5-3.4" fill="none" stroke="#1a86cc" stroke-width="0.9"/>
      <!-- globe -->
      <g fill="none" stroke="#fff" stroke-width="1">
        <circle cx="416" cy="9" r="5"/>
        <ellipse cx="416" cy="9" rx="2.2" ry="5"/>
        <line x1="411" y1="9" x2="421" y2="9"/>
      </g>
    </svg>

    <p class="contact-line">
      555.014.2200<span class="sep">|</span>555.014.2201<span class="sep">|</span>hello@maplecrestelder.com<span class="sep">|</span>www.maplecrestelder.com
    </p>
    <p class="address-line">PO BOX 4120, CEDAR HOLLOW, FL 30012</p>
  </main>
</body>
</html>
```